Need full color yard sign designed

I need a catchy yard sign to attract people whom drive by to go to the website www.brickleafappraise.net to get a free no obligation value of their home. I like to use the location icon as part of the design. The design must be in both spanish and english top and bottom split design. I have attached the template format that the printing company needs me to use. I also need it in eps format. Also the sign will be double sided so same sign will be on both sidesPlease let me know if you have any questions about the design

Target Market(s)

Home owners looking to sell

Industry/Entity Type

Real Estate

Font styles to use
Sans Serif

Colors
f68d4d
fbed22
9bcb3b
0692cd

Requirements
Must have
• call to action theme. light colors since this is a sign and must also be seen at night
Nice to have
• colorful
Should not have
• dark background, too busy

```html
<!DOCTYPE html>
<html lang="en">
<head>
<meta charset="utf-8">
<title>Brickleaf Appraise – Yard Sign</title>
<link rel="stylesheet" href="https://fonts.googleapis.com/css2?family=Figtree:wght@500&family=Open+Sans:wght@700&display=swap">
<style>
  :root {
    --sun-deep: #f3dc3a;
    --sun: #f2ec6a;
    --sun-pale: #f7f6c4;
    --band-red: #a51c24;
    --ink: #231f20;
    --pin: #262626;
    --white: #ffffff;
  }
  html, body {
    margin: 0;
    padding: 0;
    width: 1200px;
    height: 900px;
    overflow: hidden;
  }
  .yard-sign {
    position: relative;
    width: 1200px;
    height: 900px;
    overflow: hidden;
    font-family: "Figtree", "Helvetica Neue", Arial, sans-serif;
    color: var(--ink);
  }
  .sign-backdrop {
    position: absolute;
    inset: 0;
    background:
      radial-gradient(ellipse 55% 45% at 38% 50%, var(--sun-pale) 0%, rgba(247,246,196,0) 100%),
      linear-gradient(135deg, var(--sun-deep) 0%, var(--sun) 30%, var(--sun-pale) 55%, var(--sun) 80%, var(--sun-deep) 100%);
  }
  .panel {
    position: absolute;
    left: 0;
    width: 1200px;
    height: 450px;
  }
  .panel--english { top: 0; }
  .panel--spanish { top: 466px; }

  .headline {
    position: absolute;
    left: 61px;
    top: 52px;
    margin: 0;
    font-weight: 500;
    font-size: 42px;
    line-height: 56px;
    letter-spacing: 0.2px;
  }
  .url-band {
    position: absolute;
    left: 0;
    top: 216px;
    width: 984px;
    height: 68px;
    background: var(--band-red);
  }
  .url-band__text {
    position: absolute;
    left: 61px;
    top: 0;
    margin: 0;
    font-family: "Open Sans", Arial, sans-serif;
    font-weight: 700;
    font-size: 58px;
    line-height: 68px;
    letter-spacing: -1px;
    color: var(--white);
  }
  .offer {
    position: absolute;
    left: 63px;
    top: 316px;
    margin: 0;
    font-weight: 500;
    font-size: 35px;
    line-height: 44px;
    letter-spacing: 0.3px;
  }
  .location-pin {
    position: absolute;
    left: 978px;
    top: 118px;
    width: 153px;
    height: 250px;
    filter: drop-shadow(14px 12px 8px rgba(80, 60, 0, 0.35));
  }
  .panel-divider {
    position: absolute;
    left: 48px;
    top: 451px;
    width: 1128px;
    height: 2px;
    background: linear-gradient(90deg, rgba(165,28,36,0) 0%, var(--band-red) 50%, rgba(165,28,36,0) 100%);
  }
</style>
</head>
<body>
<main class="yard-sign">
  <div class="sign-backdrop" role="img" aria-label="Soft yellow faceted polygon background"></div>

  <section class="panel panel--english" lang="en">
    <h1 class="headline">How much is your home worth<br>in today’s market?</h1>
    <div class="url-band"><p class="url-band__text">www.brickleafappraise.net</p></div>
    <p class="offer">To get a free No Obligation Value of their home</p>
    <svg class="location-pin" viewBox="0 0 153 250" aria-hidden="true">
      <path fill="var(--pin)" d="M76.5 250 C62 190 0 140 0 76.5 A76.5 76.5 0 0 1 153 76.5 C153 140 91 190 76.5 250 Z"/>
      <circle cx="76.5" cy="74" r="27" fill="var(--white)"/>
    </svg>
  </section>

  <div class="panel-divider"></div>

  <section class="panel panel--spanish" lang="es">
    <h2 class="headline">Spanish text to come here<br>Spanish text to come?</h2>
    <div class="url-band"><p class="url-band__text">www.brickleafappraise.net</p></div>
    <p class="offer">To get a free No Obligation Value of their home</p>
    <svg class="location-pin" viewBox="0 0 153 250" aria-hidden="true">
      <path fill="var(--pin)" d="M76.5 250 C62 190 0 140 0 76.5 A76.5 76.5 0 0 1 153 76.5 C153 140 91 190 76.5 250 Z"/>
      <circle cx="76.5" cy="74" r="27" fill="var(--white)"/>
    </svg>
  </section>
</main>
</body>
</html>
```